New Stationary for our business

We are a gift business and would like to create a new corporate image with new stationary and design.

We would like a Classic Corporate look with a touch of Flair.

We would need:
Envelopes
Letter Head
Business Cards
With Comp Slips
Note Pads
Etc...

Our details are:

Basket Haven Pty Ltd
518 Tallow Street, Fernmead, Victoria, 3071
1800 742 918
www.baskethaven-demo.com.au
sales@baskethaven-demo.com.au

ABN: 58 603 214 796

Target Market(s)

Corporate Look

Industry/Entity Type

Marketing

Contact Information for Business Card

Basket Haven Pty Ltd
1800 742 918
518 Tallow Street
Fernmead 3071
Victoria Australia

Darren Pelluso - Managing Director
darren.pelluso@baskethaven-demo.com.au
0413 587 120

Logo Text

Basket Haven - The Gift Specialists

Colors

Designer to choose colors to be used in the design.

Requirements
Must have
• Look and Feel upmarket and exclusive

```html
<!DOCTYPE html>
<html lang="en">
<head>
<meta charset="utf-8">
<title>Basket Haven – Stationery Set</title>
<link rel="stylesheet" href="https://fonts.googleapis.com/css2?family=Arimo:wght@400;700&display=swap">
<style>
  :root {
    --violet: #4a14ff;
    --magenta: #f044f0;
    --lavender: #c9bdf4;
    --blush: #f9cbf5;
    --ink: #6a6a6a;
    --paper: #ffffff;
    --stage-light: #fafafa;
    --stage-dark: #c9c9c9;
  }
  * { box-sizing: border-box; margin: 0; padding: 0; }
  html, body { width: 1200px; height: 1200px; overflow: hidden; }
  body {
    position: relative;
    font-family: "Arimo", Arial, sans-serif;
    background: radial-gradient(circle at 50% 50%, var(--stage-light) 0%, #f0f0f0 35%, var(--stage-dark) 100%);
  }
  .sheet {
    position: absolute;
    background: var(--paper);
    overflow: hidden;
    box-shadow: 0 0 2px rgba(0,0,0,0.08);
  }
  .rule { position: absolute; }
  .rule--magenta { background: var(--magenta); }
  .rule--violet { background: var(--violet); }

  .brand {
    position: absolute;
    transform: translateX(-50%);
    text-align: center;
    white-space: nowrap;
  }
  .brand__name {
    display: block;
    font-weight: 700;
    color: var(--violet);
    text-transform: uppercase;
    letter-spacing: 0.2px;
    line-height: 1;
  }
  .brand__web {
    display: block;
    font-size: 5px;
    color: var(--ink);
    margin-top: 2px;
  }

  .artwork {
    position: absolute;
    border-radius: 40% 40% 12% 12%;
    background: linear-gradient(180deg, var(--blush) 0%, var(--blush) 55%, var(--lavender) 100%);
    opacity: 0.9;
  }

  .contact-row {
    position: absolute;
    display: flex;
    align-items: center;
    gap: 8px;
    color: var(--ink);
    font-weight: 700;
    white-space: nowrap;
  }
  .contact-row span { display: inline-flex; align-items: center; gap: 2px; }
  .icon { width: 1em; height: 1em; fill: var(--ink); flex: none; }

  .footer-band {
    position: absolute;
    right: 0;
    z-index: 2;
    background: var(--violet);
    clip-path: polygon(10px 0, 100% 0, 100% 100%, 0 100%);
    color: #fff;
    font-weight: 700;
    line-height: 1;
    white-space: nowrap;
    display: flex;
    align-items: center;
    justify-content: center;
  }
  .footer-strip { position: absolute; left: 0; right: 0; bottom: 0; background: var(--violet); }

  /* Letterhead */
  .letterhead { left: 120px; top: 171px; width: 486px; height: 679px; }
  .letterhead .brand { left: 243px; top: 48px; }
  .letterhead .brand__name { font-size: 15px; }
  .letterhead .contact-row { left: 18px; top: 650px; font-size: 5.5px; }

  /* Compliment slip */
  .comp-slip { left: 623px; top: 171px; width: 486px; height: 237px; }
  .comp-slip .brand { left: 87px; top: 37px; }
  .comp-slip .brand__name { font-size: 11px; }
  .comp-slip .contact-row { left: 18px; top: 209px; font-size: 5px; }

  /* Second letterhead */
  .letterhead-small { left: 624px; top: 421px; width: 348px; height: 485px; }
  .letterhead-small .brand { left: 173px; top: 28px; }
  .letterhead-small .brand__name { font-size: 10px; }
  .letterhead-small .brand__web { font-size: 4px; }
  .letterhead-small .contact-row { left: 12px; top: 468px; font-size: 4px; gap: 5px; }

  /* Business cards */
  .card-front {
    left: 119px; top: 870px; width: 205px; height: 137px;
    background: var(--violet);
  }
  .card-front .brand { left: 102px; top: 73px; }
  .card-front .brand__name { color: #fff; font-size: 15px; }
  .card-front .brand__web { color: var(--magenta); font-size: 6px; margin-top: 1px; }

  .card-back { left: 344px; top: 870px; width: 205px; height: 137px; }
  .card-back .brand { left: 56px; top: 67px; }
  .card-back .brand__name { font-size: 8px; }
  .card-back .divider { position: absolute; left: 100px; top: 38px; width: 1px; height: 62px; background: var(--magenta); }
  .card-details {
    position: absolute; left: 107px; top: 36px; z-index: 2;
    list-style: none; font-size: 4px; color: var(--ink); line-height: 1.35;
  }
  .card-details li { display: flex; gap: 3px; margin-bottom: 2px; }
  .card-details .icon { width: 5px; height: 5px; }
</style>
</head>
<body>

<svg width="0" height="0" style="position:absolute" aria-hidden="true">
  <symbol id="i-pin" viewBox="0 0 10 10"><path d="M5 0a3.5 3.5 0 0 0-3.5 3.5C1.5 6 5 10 5 10s3.5-4 3.5-6.5A3.5 3.5 0 0 0 5 0zm0 5a1.5 1.5 0 1 1 0-3 1.5 1.5 0 0 1 0 3z"/></symbol>
  <symbol id="i-phone" viewBox="0 0 10 10"><path d="M1 1h8v2H1zM2 4h6l1 5H1z"/></symbol>
  <symbol id="i-mail" viewBox="0 0 10 10"><path d="M0 2h10v6H0zm1 1v.4l4 2.6 4-2.6V3z"/></symbol>
  <symbol id="i-globe" viewBox="0 0 10 10"><path d="M5 0a5 5 0 1 0 0 10A5 5 0 0 0 5 0zm0 1.2a3.8 3.8 0 1 1 0 7.6 3.8 3.8 0 0 1 0-7.6z"/></symbol>
</svg>

<!-- Letterhead -->
<section class="sheet letterhead" aria-label="Letterhead">
  <div class="rule rule--magenta" style="left:0;top:38px;width:180px;height:6px"></div>
  <div class="rule rule--violet" style="right:0;top:38px;width:178px;height:6px"></div>
  <div class="brand">
    <span class="brand__name">Basket Haven</span>
    <span class="brand__web">www.baskethaven-demo.com.au</span>
  </div>
  <div class="artwork" role="img" aria-label="Faint illustration of two open hands holding a wrapped gift box" style="left:7px;top:440px;width:232px;height:192px"></div>
  <div class="rule rule--magenta" style="left:14px;top:646px;width:310px;height:1px"></div>
  <div class="contact-row">
    <span><svg class="icon"><use href="#i-pin"/></svg>518 Tallow Street, Fernmead, Victoria, 3071</span>
    <span><svg class="icon"><use href="#i-phone"/></svg>1800 742 918</span>
    <span><svg class="icon"><use href="#i-mail"/></svg>sales@baskethaven-demo.com.au</span>
  </div>
  <div class="footer-band" style="top:648px;width:163px;height:17px;font-size:9.5px">www.baskethaven-demo.com.au</div>
  <div class="footer-strip" style="height:14px"></div>
</section>

<!-- Compliment slip -->
<section class="sheet comp-slip" aria-label="Compliment slip">
  <div class="rule rule--magenta" style="left:4px;top:34px;width:33px;height:5px"></div>
  <div class="rule rule--violet" style="left:135px;right:0;top:34px;height:5px"></div>
  <div class="brand">
    <span class="brand__name">Basket Haven</span>
    <span class="brand__web">www.baskethaven-demo.com.au</span>
  </div>
  <div class="artwork" role="img" aria-label="Faint illustration of two open hands holding a wrapped gift box" style="left:0;top:77px;width:152px;height:130px"></div>
  <div class="rule" style="left:0;top:207px;width:330px;height:1px;background:var(--ink)"></div>
  <div class="contact-row">
    <span><svg class="icon"><use href="#i-pin"/></svg>518 Tallow Street, Fernmead, Victoria, 3071</span>
    <span><svg class="icon"><use href="#i-phone"/></svg>1800 742 918</span>
    <span><svg class="icon"><use href="#i-mail"/></svg>sales@baskethaven-demo.com.au</span>
  </div>
  <div class="footer-band" style="top:207px;width:159px;height:17px;font-size:8.5px">www.baskethaven-demo.com.au</div>
  <div class="footer-strip" style="height:13px"></div>
</section>

<!-- Second letterhead -->
<section class="sheet letterhead-small" aria-label="Letterhead, compact format">
  <div class="rule rule--magenta" style="left:0;top:26px;width:128px;height:4px"></div>
  <div class="rule rule--violet" style="right:0;top:26px;width:128px;height:4px"></div>
  <div class="brand">
    <span class="brand__name">Basket Haven</span>
    <span class="brand__web">www.baskethaven-demo.com.au</span>
  </div>
  <div class="artwork" role="img" aria-label="Faint illustration of two open hands holding a wrapped gift box" style="left:7px;top:315px;width:162px;height:146px"></div>
  <div class="rule rule--magenta" style="left:8px;top:465px;width:230px;height:1px"></div>
  <div class="contact-row">
    <span><svg class="icon"><use href="#i-pin"/></svg>518 Tallow Street, Fernmead, Victoria, 3071</span>
    <span><svg class="icon"><use href="#i-mail"/></svg>sales@baskethaven-demo.com.au</span>
  </div>
  <div class="footer-band" style="top:465px;width:114px;height:12px;font-size:6.5px">www.baskethaven-demo.com.au</div>
  <div class="footer-strip" style="height:8px"></div>
</section>

<!-- Business card, front -->
<section class="sheet card-front" aria-label="Business card front">
  <div class="brand">
    <span class="brand__name">Basket Haven</span>
    <span class="brand__web">www.baskethaven-demo.com.au</span>
  </div>
</section>

<!-- Business card, back -->
<section class="sheet card-back" aria-label="Business card back">
  <div class="brand"><span class="brand__name">Basket Haven</span></div>
  <div class="divider"></div>
  <ul class="card-details">
    <li>Basket Haven Pty Ltd</li>
    <li><svg class="icon"><use href="#i-pin"/></svg>518 Tallow Street, Fernmead<br>Victoria, 3071</li>
    <li><svg class="icon"><use href="#i-phone"/></svg>1800 742 918</li>
    <li><svg class="icon"><use href="#i-mail"/></svg>sales@baskethaven-demo.com.au</li>
    <li><svg class="icon"><use href="#i-globe"/></svg>www.baskethaven-demo.com.au</li>
  </ul>
  <div class="artwork" role="img" aria-label="Faint illustration of two open hands holding a wrapped gift box" style="left:162px;top:88px;width:42px;height:35px"></div>
  <div class="footer-strip" style="height:14px"></div>
</section>

</body>
</html>
```